Flyer für einen Pflegedienst
Zielgruppe
Wir sind ein Pflegedienst, unsere Zielgruppe sind alle Menschen die Unterstützung brauchen. Das sind im Hauptteil Senioren.
Aufgabenstellung
Der Flyer soll im DIN A5 Format designed sein. Der Print soll hochwertig sein. Wir möchten vor allem wohlhabendere Kunden damit ansprechen. Er soll die Kunden direkt packen, aber auch nicht zu viele Informationen beinhalten, die einen überfordern.

```html
<!DOCTYPE html>
<html lang="de">
<head>
<meta charset="utf-8">
<title>Pflege Wane – Flyer</title>
<link rel="stylesheet" href="https://fonts.googleapis.com/css2?family=Nunito:ital,wght@0,400;0,700;0,800;1,400&display=swap">
<style>
:root{
  --blue:#6e8fb7;
  --blue-head:#5b80b0;
  --grey-band:#d5d9dc;
  --cream:#fbfaf5;
  --ink:#2f2f2f;
  --frame:#8a8a8a;
  --white:#ffffff;
}
*{box-sizing:border-box;margin:0;padding:0}
html,body{width:1200px;height:852px;overflow:hidden;background:var(--white)}
body{position:relative;font-family:"Nunito",sans-serif;color:var(--ink)}
.page{position:absolute;top:15px;width:582px;height:823px;background:var(--cream);border:2px solid var(--frame);overflow:hidden}
.page--front{left:11px}
.page--back{left:607px}
.photo{position:absolute;left:0;top:0;width:100%}
.page--front .photo{height:394px;background:linear-gradient(135deg,#e9e6df 0%,#d9d4ca 35%,#b9c7d9 60%,#c9b8a0 100%)}
.page--back .photo{height:285px;background:linear-gradient(120deg,#c8d3dc 0%,#2f55a0 35%,#b7c6b3 65%,#d7c7a6 100%)}
.band{position:absolute;left:0;width:100%;background:var(--blue)}
.band-grey{position:absolute;right:0;background:var(--grey-band)}
.page--front .band{top:394px;height:20px}
.page--front .band-grey{top:414px;left:99px;height:13px}
.page--back .band{top:285px;height:22px}
.page--back .band-grey{top:307px;left:99px;height:13px}
.brand-name{position:absolute;color:var(--white);font-weight:700;white-space:nowrap}
.page--front .brand-name{left:194px;top:308px;font-size:40px;line-height:48px}
.page--back .brand-name{left:420px;top:238px;font-size:24px;line-height:30px}
.content{position:absolute;left:50px;right:50px}
.page--front .content{top:455px}
h2{color:var(--blue-head);font-weight:800;font-size:19.5px;margin-bottom:8px}
.content p{font-size:16px;letter-spacing:.15px;line-height:19.7px;margin-bottom:20px}
.footer{position:absolute;left:0;bottom:0;width:100%;height:116px;background:var(--blue);color:var(--white)}
.contact{position:absolute;font-size:15px;line-height:23.5px}
.contact li{list-style:none;display:flex;align-items:center;gap:6px}
.contact svg{width:15px;height:15px;flex:none}
.contact--address{left:55px;top:22px}
.contact--address .name{font-weight:700;padding-left:21px}
.contact--address .indent{padding-left:21px}
.contact--online{left:302px;top:22px}
.page--back .content{top:348px;left:50px;right:30px}
.service h3{font-style:italic;font-weight:400;font-size:17px;margin-bottom:4px}
.service{margin-bottom:19px}
.service ul{list-style:none}
.service li{font-size:16px;line-height:19.8px;padding-left:24px;position:relative}
.service li::before{content:"";position:absolute;left:2px;top:8px;width:6px;height:6px;border-radius:50%;background:var(--ink)}
.footer-col{position:absolute;top:12px}
.footer-col h4{font-size:13.5px;font-weight:800;margin-bottom:6px}
.footer-col li,.footer-col p{font-size:13px;line-height:16.7px;list-style:none}
.footer-col--steps{left:50px}
.footer-col--steps li{padding-left:24px;position:relative}
.footer-col--steps li::before{content:"";position:absolute;left:2px;top:7px;width:4px;height:4px;border-radius:50%;background:var(--white)}
.footer-divider{position:absolute;left:316px;top:12px;width:1px;height:90px;background:var(--white)}
.footer-col--care{left:330px;width:205px}
</style>
</head>
<body>

<section class="page page--front">
  <div class="photo" role="img" aria-label="Foto: Pflegerin legt einer älteren Dame lächelnd die Hände auf die Schultern, helle Küche im Hintergrund"></div>
  <div class="brand-name">Pflege Wane</div>
  <div class="band"></div>
  <div class="band-grey"></div>
  <div class="content">
    <h2>Gemeinsam leben, liebevoll pflegen</h2>
    <p><em>Pflege Wane</em> - Wir sind Ihr zuverlässiger ambulanter Pflegedienst für Mülheim an der Ruhr, Süd-Duisburg, Süd- &amp; West-Essen, Süd-Oberhausen, Ratingen &amp; Lintorf.</p>
    <p>Mit dem Grundsatz <em>„Gemeinsam leben, liebevoll pflegen“</em> verpflichten wir uns, jedem Patienten nicht nur professionelle Pflege, sondern auch ein Gefühl von familiärer Geborgenheit und Respekt zu bieten. In dieser Atmosphäre des Vertrauens möchten wir unseren Patienten und ihren Familien Sicherheit und eine stetige Verbesserung der Lebensqualität bieten.</p>
  </div>
  <footer class="footer">
    <ul class="contact contact--address">
      <li class="name">Pflege Wane</li>
      <li><svg viewBox="0 0 16 16" fill="none" stroke="#fff" stroke-width="1.3"><path d="M2 8 8 2.5 14 8M4 7v6.5h8V7"/></svg>Lindenhof-Straße 27b</li>
      <li class="indent">45479 Mülheim an der Ruhr</li>
    </ul>
    <ul class="contact contact--online">
      <li><svg viewBox="0 0 16 16" fill="none" stroke="#fff" stroke-width="1.3"><path d="M3 2h3l1 3.5-2 1.2a8 8 0 0 0 4.3 4.3l1.2-2 3.5 1v3c-6 .5-11.5-5-11-11z"/></svg>0208 - 51237700</li>
      <li><svg viewBox="0 0 16 16" fill="none" stroke="#fff" stroke-width="1.2"><circle cx="8" cy="8" r="6.3"/><path d="M1.7 8h12.6M8 1.7c-3 3.5-3 9 0 12.6M8 1.7c3 3.5 3 9 0 12.6"/></svg>www.pflegewane.de</li>
      <li><svg viewBox="0 0 16 16" fill="none" stroke="#fff" stroke-width="1.2"><rect x="1.5" y="3.5" width="13" height="9"/><path d="m1.5 3.5 6.5 5 6.5-5"/></svg>info@pflegewane.de</li>
    </ul>
  </footer>
</section>

<section class="page page--back">
  <div class="photo" role="img" aria-label="Foto: Pflegerin in blauer Kleidung serviert einer älteren Dame mit Tablet ein Frühstück mit Orangensaft"></div>
  <div class="brand-name">Pflege Wane</div>
  <div class="band"></div>
  <div class="band-grey"></div>
  <div class="content">
    <h2>Das können wir für Sie tun:</h2>
    <div class="service">
      <h3>Behandlungspflege</h3>
      <ul>
        <li>Professionelle Wundversorgung und Verbandswechsel</li>
        <li>Zuverlässige Medikamentengabe und Injektionen</li>
        <li>Auf individuelle Bedürfnisse abgestimmte Pflege</li>
      </ul>
    </div>
    <div class="service">
      <h3>Grundpflege</h3>
      <ul>
        <li>Assistenz bei Routinen (Baden, Ankleiden und Körperpflege)</li>
        <li>Unterstützung bei Mobilität und Erhalt der Selbstständigkeit</li>
        <li>Hilfe bei Nahrungs- und Flüssigkeitsaufnahme</li>
      </ul>
    </div>
    <div class="service">
      <h3>Betreuung &amp; Hauswirtschaft</h3>
      <ul>
        <li>Unterstützung bei hauswirtschaftlichen Aufgaben</li>
        <li>Hilfe bei Einkäufen oder Behördengängen</li>
        <li>Gemeinsame Aktivitäten und sozialer Austausch</li>
      </ul>
    </div>
  </div>
  <footer class="footer">
    <div class="footer-col footer-col--steps">
      <h4>So schnell kommt unser Pflegedienst:</h4>
      <ul>
        <li>Rufen Sie uns an: 0208 - 512 377 00</li>
        <li>Wir kommen bei Ihnen vorbei</li>
        <li>Sie erhalten ein Angebot</li>
        <li>Die Pflege beginnt am nächsten Tag</li>
      </ul>
    </div>
    <div class="footer-divider"></div>
    <div class="footer-col footer-col--care">
      <h4>Sie liegen uns am Herzen.</h4>
      <p>Daher werden Patienten bei uns ohne lange Wartezeiten aufgenommen.</p>
    </div>
  </footer>
</section>

</body>
</html>
```